Varnel Group Limited Stationary

We are in need of business card and letterhead designs. We are looking for clean modern designs that complement the style and feel of our logo.

Industry/Entity Type

Business

```html
<!DOCTYPE html>
<html lang="en">
<head>
<meta charset="utf-8">
<title>Varnel Group Limited – Business Card</title>
<link href="https://fonts.googleapis.com/css2?family=Questrial&display=swap" rel="stylesheet">
<style>
  :root {
    --backdrop: #2a2a2c;
    --brand-blue: #0b4595;
    --brand-blue-soft: #1f5aa8;
    --slate: #55575c;
    --ink: #1d1d1f;
    --paper: #ffffff;
    --paper-shade: #eeeeee;
  }
  * { margin: 0; padding: 0; box-sizing: border-box; }
  html, body { width: 1200px; height: 900px; overflow: hidden; }
  body {
    background: var(--backdrop);
    font-family: "Questrial", "Century Gothic", sans-serif;
    position: relative;
  }
  .card {
    position: absolute;
    width: 760px;
    height: 434px;
    overflow: hidden;
    box-shadow: 0 18px 40px rgba(0,0,0,0.55);
  }
  /* Back side */
  .card-back {
    left: 110px; top: 60px;
    background: var(--brand-blue);
  }
  .card-back .faint-circle {
    position: absolute;
    left: 40px; top: 150px;
    width: 380px; height: 380px;
    border-radius: 50%;
    background: var(--brand-blue-soft);
    opacity: 0.55;
  }
  .card-back .brand {
    position: absolute;
    left: 430px; top: 120px;
    display: flex; align-items: center; gap: 14px;
    color: var(--paper);
  }
  .card-back .brand-mark {
    width: 46px; height: 46px; border-radius: 50%;
    background: var(--paper);
  }
  .card-back .brand-name { font-size: 34px; letter-spacing: 1px; }
  .card-back .brand-rule {
    position: absolute; left: 470px; top: 180px;
    width: 240px; height: 1px; background: rgba(255,255,255,0.7);
  }

  /* Front side */
  .card-front {
    left: 330px; top: 410px;
    background: linear-gradient(90deg, var(--paper) 0%, var(--paper) 60%, var(--paper-shade) 100%);
  }
  .card-front .brand {
    position: absolute;
    left: 50px; top: 150px;
    display: flex; align-items: center; gap: 16px;
  }
  .card-front .brand-mark {
    width: 62px; height: 62px; border-radius: 50%;
    background: var(--brand-blue);
  }
  .card-front .brand-name {
    font-size: 40px; color: var(--brand-blue); letter-spacing: 1px;
  }
  .card-front .brand-rule {
    position: absolute; left: 70px; top: 230px;
    width: 280px; height: 1px; background: #b9c4d6;
  }
  .contact {
    position: absolute;
    left: 430px; top: 58px;
    color: var(--ink);
    text-transform: none;
  }
  .contact .holder {
    font-size: 15px; letter-spacing: 4px; font-weight: 700;
    text-transform: uppercase;
  }
  .contact .role { color: var(--brand-blue); font-weight: 400; letter-spacing: 3px; font-size: 13px; }
  .contact .address {
    margin-top: 26px;
    font-size: 13px; letter-spacing: 3px; line-height: 1.5;
    text-transform: uppercase; color: #333;
  }
  .contact .lines { margin-top: 18px; list-style: none; }
  .contact .lines li {
    display: flex; align-items: center; gap: 18px;
    font-size: 14px; letter-spacing: 2px; color: #333;
    height: 22px;
  }
  .contact .lines svg { width: 14px; height: 14px; fill: var(--brand-blue); flex: none; }
  .card-front .footer-bands { position: absolute; left: 0; bottom: 0; }
</style>
</head>
<body>

<section class="card card-back" aria-label="Business card, back">
  <div class="faint-circle"></div>
  <div class="brand">
    <span class="brand-mark"></span>
    <span class="brand-name">Varnel Group</span>
  </div>
  <div class="brand-rule"></div>
</section>

<section class="card card-front" aria-label="Business card, front">
  <div class="brand">
    <span class="brand-mark"></span>
    <span class="brand-name">Varnel Group</span>
  </div>
  <div class="brand-rule"></div>

  <div class="contact">
    <p class="holder">Maren Holt <span class="role">&nbsp;-&nbsp; Director</span></p>
    <p class="address">Shop 2, 318-322 Carden<br>Road Westbury North</p>
    <ul class="lines">
      <li>
        <svg viewBox="0 0 16 16" aria-hidden="true"><path d="M2 6c0-2 3-3 6-3s6 1 6 3v1h-3V5.5H5V7H2zM4 8h8l1 5H3z"/></svg>
        9517 2804
      </li>
      <li>
        <svg viewBox="0 0 16 16" aria-hidden="true"><path d="M4 1h8v4H4zM1 6h14v6h-3v3H4v-3H1zM5 10v3h6v-3z"/></svg>
        9517 2866
      </li>
      <li>
        <svg viewBox="0 0 16 16" aria-hidden="true"><path d="M1 3h14v10H1zM2.5 4.5L8 9l5.5-4.5v-.1h-11z"/></svg>
        maren@varnelgroup.com
      </li>
      <li>
        <svg viewBox="0 0 16 16" aria-hidden="true"><path d="M8 1a7 7 0 100 14A7 7 0 008 1zm0 1.5c.8 0 1.6 1.6 1.9 4H6.1c.3-2.4 1.1-4 1.9-4zM2.6 7.5h2.1a12 12 0 000 1H2.6a5.5 5.5 0 010-1zm3.5 2h3.8c-.3 2.4-1.1 4-1.9 4s-1.6-1.6-1.9-4zm5.2-2h2.1a5.5 5.5 0 010 1h-2.1a12 12 0 000-1z"/></svg>
        www.varnelgroup.com
      </li>
    </ul>
  </div>

  <svg class="footer-bands" width="760" height="90" viewBox="0 0 760 90" aria-hidden="true">
    <polygon points="0,54 458,54 432,90 0,90" fill="var(--brand-blue)"/>
    <polygon points="490,12 760,12 760,90 440,90" fill="var(--slate)"/>
  </svg>
</section>

</body>
</html>
```